Cognitive therapist.

I am a therapist and my main work is with clients who have depression and anxiety disorders.

I need something reasonably plain. Cognitive therapy is a very pragmatic approach to dealing with problems, so it isn't new agey (no offence to new age therapies at all)

Hi everyone, I am currently looking at a particular design that I will most likely go with. Cheers, Mel

Mel Tarrow
Cognitive Therapist
BA, PG Dip Mental Health,
PG Dip Cog Beh Therapy
MKLPT

The Larchmont Rooms,
Level One
57 Quillon Parade
Cnr Fenwick St & Quillon Parade
P O Box 38 215
WELLINGTON 6281

Phone: 027 534 2870 Email: mtarrow@vexmail.co.nz

www.meltarrow.co.nz

• No illustration, or colour. not old style fonts.

```html
<!DOCTYPE html>
<html lang="en">
<head>
<meta charset="utf-8">
<title>Mel Tarrow – Business Card</title>
<link rel="stylesheet" href="https://fonts.googleapis.com/css2?family=Source+Sans+3:ital,wght@0,400;0,600;1,400&display=swap">
<style>
  :root {
    --backdrop: #b3283f;
    --card-blue: #0c79ad;
    --name-light: #8fd3f2;
    --name-deep: #1a6fb8;
    --band-grey: #9a9c9e;
    --text-grey: #6d6e70;
    --paper: #ffffff;
    --photo-light: #cfcfcf;
    --photo-dark: #5a5a5a;
  }
  * { margin: 0; padding: 0; box-sizing: border-box; }
  html, body { width: 1200px; height: 900px; overflow: hidden; }
  body {
    background: var(--backdrop);
    font-family: "Source Sans 3", "Myriad Pro", sans-serif;
    position: relative;
  }
  .card {
    position: absolute;
    top: 305px;
    width: 520px;
    height: 290px;
    box-shadow: 0 6px 14px rgba(0,0,0,0.25);
    overflow: hidden;
  }
  /* back side */
  .card--back {
    left: 60px;
    background: var(--card-blue);
    display: flex;
    flex-direction: column;
    align-items: center;
    justify-content: center;
  }
  .card--back .name {
    color: var(--name-light);
    font-weight: 600;
    font-size: 50px;
    line-height: 1;
    letter-spacing: 0.5px;
  }
  .card--back .title {
    color: var(--name-light);
    font-style: italic;
    font-size: 27px;
    line-height: 1.1;
    margin-top: 0;
  }
  /* front side */
  .card--front { left: 620px; background: var(--paper); }
  .front-top {
    position: absolute; left: 0; top: 0;
    width: 100%; height: 186px;
    background: var(--paper);
  }
  .front-top .corner-name {
    position: absolute; left: 26px; top: 14px;
    color: var(--name-deep);
  }
  .corner-name .name { font-weight: 600; font-size: 24px; line-height: 1; }
  .corner-name .title { font-style: italic; font-size: 14px; line-height: 1.1; }
  .credentials {
    position: absolute; left: 40px; top: 94px;
    width: 360px;
    text-align: center;
    color: var(--text-grey);
    font-style: italic;
    font-size: 14px;
    line-height: 20px;
  }
  .portrait {
    position: absolute; right: 0; top: 0;
    width: 130px; height: 186px;
    background: linear-gradient(180deg, var(--photo-light) 0%, var(--photo-dark) 100%);
  }
  .grey-band {
    position: absolute; left: 0; top: 186px;
    width: 100%; height: 15px;
    background: var(--band-grey);
  }
  .front-bottom {
    position: absolute; left: 0; top: 201px;
    width: 100%; height: 89px;
    background: var(--card-blue);
    color: var(--paper);
  }
  .contact-list {
    list-style: none;
    position: absolute; left: 24px; top: 6px;
    font-size: 14px;
    line-height: 19.5px;
  }
  .contact-list li { display: flex; align-items: center; gap: 2px; }
  .contact-list svg { width: 12px; height: 12px; fill: var(--paper); }
  .front-bottom .sign-off {
    position: absolute; right: 26px; top: 4px;
    text-align: center;
  }
  .sign-off .name { font-weight: 600; font-size: 29px; line-height: 1.1; letter-spacing: 0.3px; }
  .sign-off .title { font-style: italic; font-size: 14px; line-height: 1.1; }
</style>
</head>
<body>
  <section class="card card--back">
    <div class="name">Mel Tarrow</div>
    <div class="title">Cognitive Therapist BA</div>
  </section>

  <section class="card card--front">
    <div class="front-top">
      <div class="corner-name">
        <div class="name">Mel Tarrow</div>
        <div class="title">Cognitive Therapist BA</div>
      </div>
      <p class="credentials">
        PG Dip Mental Health, PG Dip Cog Beh Therapy<br>
        MKLPT The Larchmont Rooms, Level One 57 Quillon Parade<br>
        Cnr Fenwick St &amp; Quillon Parade
      </p>
      <div class="portrait" role="img" aria-label="Black and white portrait photograph of the therapist"></div>
    </div>
    <div class="grey-band"></div>
    <div class="front-bottom">
      <ul class="contact-list">
        <li><svg viewBox="0 0 12 12"><path d="M6 0.5a3.6 3.6 0 0 1 3.6 3.6C9.6 6.8 6 11.5 6 11.5S2.4 6.8 2.4 4.1A3.6 3.6 0 0 1 6 0.5z"/></svg>: 38215 Wellington 6281</li>
        <li><svg viewBox="0 0 12 12"><path d="M1 4c0-2 2-3 5-3s5 1 5 3v1H8.5V3.8h-5V5H1zM3 6h6l1.5 5h-9z"/></svg>: 027 534 2870</li>
        <li><svg viewBox="0 0 12 12"><path d="M1 3h10v7H1zM1.8 3.6 6 7l4.2-3.4"/></svg>: mtarrow@vexmail.co.nz</li>
        <li><svg viewBox="0 0 12 12"><circle cx="6" cy="6" r="5"/></svg>: www.meltarrow.co.nz</li>
      </ul>
      <div class="sign-off">
        <div class="name">Mel Tarrow</div>
        <div class="title">Cognitive Therapist&nbsp; BA</div>
      </div>
    </div>
  </section>
</body>
</html>
```